Business Card Design for DJ

Double-sided full colour business card, with containing the following key information:

DJ Marblequake
Phone (###) ###-####
Email: djmarblequake@pelnomail.net
Friendlinq: friendlinq.net/djmarblequake
Chirper: @djmarblequake

Bringing you the best in Top 40 - Retro - Funk

"It's gonna be a marblequake."

Club/Bar – Weddings – Private Parties - Corporate Events
3000W of portable sound
Dancefloor lighting with optional custom gobos
Available HD Projector and screen
Available custom video production
Free consultation

ORMB Licensed (small logo from http://www.ormb-rights.ca)
Member of TVSKE (small logo from http://www.tvske-guild.ca)

Requirements
Must have
• DJ Marblequake logo (attached) or alternative wordmark using type similar to CLUBLAND at http://tunevaultzone.net/uploads/posts/1226228091_6705615x.jpg
Nice to have
• headshot (attached), dance club look/feel

```html
<!DOCTYPE html>
<html lang="en">
<head>
<meta charset="utf-8">
<title>DJ Marblequake – Business Card</title>
<link rel="stylesheet" href="https://fonts.googleapis.com/css2?family=Crimson+Text:wght@400&family=Fira+Sans+Condensed:ital,wght@1,600&display=swap">
<style>
  :root {
    --sheet: #f7faf9;
    --ink: #111111;
    --night: #050607;
    --teal: #46a595;
    --teal-deep: #2c4b48;
    --teal-mist: #5f9f94;
    --glow: rgba(120, 210, 198, 0.35);
    --red: #ff1a1a;
    --white: #ffffff;
    --crowd: #08090b;
  }
  * { margin: 0; padding: 0; box-sizing: border-box; }
  html, body { width: 1200px; height: 1020px; overflow: hidden; background: var(--sheet); }
  .sheet { position: relative; width: 1200px; height: 1020px; font-family: "Crimson Text", Georgia, serif; color: var(--ink); }

  .card-front { position: absolute; left: 0; top: 0; width: 891px; height: 510px; background: var(--teal); }
  .front-face { position: absolute; left: 19px; top: 0; width: 846px; height: 480px; overflow: hidden;
    background: linear-gradient(180deg, #0c0f10 0%, #151b1c 30%, #3a6f69 46%, #48a496 56%, var(--night) 68%, var(--night) 100%); }
  .stage-glow { position: absolute; left: 520px; top: 140px; width: 300px; height: 140px;
    background: radial-gradient(ellipse at 50% 70%, var(--glow) 0%, rgba(120,210,198,0) 70%); }
  .headshot { position: absolute; left: 8px; top: 20px; width: 150px; height: 190px; border-radius: 50% 50% 44% 44%;
    background: radial-gradient(circle at 50% 35%, #9a8a80 0%, #4a4644 45%, #121314 80%); }
  .crowd-front { position: absolute; left: 0; top: 222px; width: 846px; height: 258px;
    background: linear-gradient(180deg, rgba(10,12,14,0) 0%, #0a0c0e 25%, var(--crowd) 60%); }
  .tagline { position: absolute; right: 14px; top: 24px; font-family: "Fira Sans Condensed", "Arial Narrow", sans-serif;
    font-style: italic; font-weight: 600; font-size: 30px; line-height: 36px; color: var(--red); letter-spacing: -0.5px; white-space: nowrap; }
  .wordmark { position: absolute; right: 14px; top: 62px; font-size: 86px; font-weight: 400; line-height: 1; color: var(--red); white-space: nowrap; }
  .contact { position: absolute; right: 18px; top: 306px; list-style: none; text-align: right;
    font-family: "Fira Sans Condensed", "Arial Narrow", sans-serif; font-style: italic; font-weight: 600;
    font-size: 24px; line-height: 39.5px; color: var(--white); }

  .card-back { position: absolute; left: 0; top: 510px; width: 891px; height: 510px; overflow: hidden;
    background: radial-gradient(ellipse at 70% 70%, #6bb0a4 0%, var(--teal-mist) 30%, var(--teal-deep) 75%, #1e2e2d 100%); }
  .crowd-back { position: absolute; left: 0; bottom: 0; width: 891px; height: 130px;
    background: linear-gradient(180deg, rgba(6,8,9,0) 0%, rgba(6,8,9,0.85) 40%, var(--crowd) 70%); }
  .slogan { position: absolute; left: 78px; top: 46px; font-size: 35px; color: var(--white); }
  .services { position: absolute; left: 113px; top: 121px; list-style: none; font-size: 28px; line-height: 38px; color: var(--white); }
  .services li:nth-child(4) { margin-top: 5px; }
  .offer { position: absolute; left: 78px; top: 336px; font-size: 29px; color: var(--red); }
  .member-badge { position: absolute; left: 747px; top: 445px; width: 99px; height: 36px; background: var(--white); }

  .label { position: absolute; font-size: 25px; color: var(--ink); }
  .label-front { left: 898px; top: 4px; }
  .label-back { left: 905px; top: 522px; }
  .note { position: absolute; left: 911px; top: 228px; font-size: 26px; line-height: 38px; color: var(--ink); white-space: nowrap; }
</style>
</head>
<body>
<main class="sheet">
  <section class="card-front">
    <div class="front-face">
      <div class="stage-glow" role="img" aria-label="Soft stage light glow over the crowd"></div>
      <div class="crowd-front" role="img" aria-label="Silhouetted crowd with raised hands"></div>
      <div class="headshot" role="img" aria-label="Headshot of the DJ wearing headphones"></div>
      <p class="tagline">Bringing you the best in Top 40 - Retro - Funk</p>
      <h1 class="wordmark">DJ Marblequake</h1>
      <ul class="contact">
        <li>Phone: (###) ### ####</li>
        <li>Email: djmarblequake@pelnomail.net</li>
        <li>Friendlinq: friendlinq.net/djmarblequake</li>
        <li>Chirper: @djmarblequake</li>
      </ul>
    </div>
  </section>

  <section class="card-back">
    <div class="crowd-back" role="img" aria-label="Silhouetted crowd with raised hands"></div>
    <p class="slogan">“It’s gonna be a marblequake”</p>
    <ul class="services">
      <li>Club/Bar ~ Weddings ~ Private Parties ~ Corporate Events</li>
      <li>3000W of portable sound</li>
      <li>Dancefloor lighting with optional custom gobos</li>
      <li>Available HD Projector and screen</li>
      <li>Available custom video production</li>
    </ul>
    <p class="offer">Free consultation</p>
    <div class="member-badge" role="img" aria-label="TVSKE membership badge"></div>
  </section>

  <p class="label label-front">Front</p>
  <p class="note">(just a note,<br>http://www.ormb-rights.ca<br>is undergoing changes<br>so I was not able to<br>obtain their logo yet.)</p>
  <p class="label label-back">Back</p>
</main>
</body>
</html>
```